PELTON RIDGE HEATING AND COOLING

Industry/Entity Type

Hvac

Requirements
Must have
• logo
My name: Doug Ferriblen
Phone number 555-304-9461
Text:
Furnace and AC repairs
New furnace and AC installation
Ductwork
Gas lines
Water Tanks
Tankless water heaters
Nice to have
• Profesional modern look

```html
<!DOCTYPE html>
<html lang="en">
<head>
<meta charset="utf-8">
<title>Pelton Ridge Heating and Cooling – Business Card</title>
<link rel="stylesheet" href="https://fonts.googleapis.com/css2?family=Montserrat:wght@400;600;700&display=swap">
<style>
  :root {
    --blue: #0a6eb4;
    --navy: #1a4f9c;
    --red: #cf2027;
    --green: #74b943;
    --paper: #f4f4f4;
    --stage: #e3e3e3;
    --grey: #6f6f6f;
    --white: #ffffff;
  }
  * { margin: 0; padding: 0; box-sizing: border-box; }
  html, body { width: 1200px; height: 960px; overflow: hidden; }
  body {
    background: var(--stage);
    font-family: "Montserrat", Arial, sans-serif;
    position: relative;
  }
  .card {
    position: absolute;
    left: 297px;
    width: 605px;
    height: 345px;
    background: var(--paper);
    overflow: hidden;
  }
  .card-front { top: 107px; }
  .card-back { top: 505px; }
  .card-shapes { position: absolute; inset: 0; }

  .brand-name {
    position: absolute;
    color: var(--navy);
    font-weight: 600;
    text-align: center;
    line-height: 1.15;
  }
  .brand-name .brand-main { display: block; letter-spacing: 1px; }
  .brand-name .brand-sub { display: block; letter-spacing: 1.5px; }

  .card-front .brand-name { left: 0; right: 0; top: 150px; }
  .card-front .brand-main { font-size: 40px; }
  .card-front .brand-sub { font-size: 16px; margin-top: 4px; }

  .web-pill {
    position: absolute;
    left: 193px; top: 258px;
    width: 218px; height: 24px;
    background: var(--green);
    border-radius: 6px;
    color: var(--white);
    font-size: 15px;
    text-align: center;
    line-height: 24px;
  }
  .tagline {
    position: absolute;
    left: 0; right: 0; top: 300px;
    text-align: center;
    color: var(--white);
    font-weight: 700;
    font-size: 19px;
  }

  .card-back .brand-name { left: 20px; width: 280px; top: 140px; }
  .card-back .brand-main { font-size: 28px; }
  .card-back .brand-sub { font-size: 12px; margin-top: 3px; }

  .contact {
    position: absolute;
    right: 35px; top: 44px;
    text-align: right;
    color: var(--white);
  }
  .contact-name { color: var(--green); font-weight: 700; font-size: 20px; letter-spacing: 0.5px; }
  .contact-line { display: flex; justify-content: flex-end; align-items: center; gap: 4px; font-size: 15px; line-height: 20px; }
  .contact-phone { font-weight: 700; font-size: 18px; margin-top: 22px; line-height: 22px; }
  .contact-line svg { width: 13px; height: 13px; }
  .divider { width: 45px; height: 3px; background: var(--white); margin: 16px 0 16px auto; }
  .services { list-style: none; font-size: 15px; line-height: 19.2px; }
</style>
</head>
<body>

<section class="card card-front">
  <svg class="card-shapes" viewBox="0 0 605 345" aria-hidden="true">
    <rect width="605" height="345" fill="var(--paper)"/>
    <path d="M0 0 H605 V135 Q302 108 0 135 Z" fill="var(--blue)"/>
    <path d="M0 275 Q302 250 605 275 V345 H0 Z" fill="var(--green)"/>
    <path d="M0 287 Q302 262 605 287 V345 H0 Z" fill="var(--red)"/>
  </svg>
  <div class="brand-name">
    <span class="brand-main">PELTON RIDGE</span>
    <span class="brand-sub">HEATING AND COOLING</span>
  </div>
  <div class="web-pill">www.PeltonRidge.ca</div>
  <p class="tagline">An Expert HVAC Contractor</p>
</section>

<section class="card card-back">
  <svg class="card-shapes" viewBox="0 0 605 345" aria-hidden="true">
    <rect width="605" height="345" fill="var(--paper)"/>
    <path d="M244 0 C318 80 330 250 252 345 H605 V0 Z" fill="var(--green)"/>
    <path d="M228 345 C290 270 305 200 306 140 C312 230 295 295 262 345 Z" fill="var(--red)"/>
    <path d="M262 0 C336 80 346 250 268 345 H605 V0 Z" fill="var(--blue)" stroke="var(--white)" stroke-width="2"/>
  </svg>
  <div class="brand-name">
    <span class="brand-main">PELTON RIDGE</span>
    <span class="brand-sub">HEATING AND COOLING</span>
  </div>
  <div class="contact">
    <p class="contact-name">DOUG FERRIBLEN</p>
    <p class="contact-line contact-phone">555-304-9461
      <svg viewBox="0 0 16 16" aria-hidden="true"><path d="M3 1.5 L6 1 L7.5 5 L5.5 6.5 C6.5 8.5 7.5 9.5 9.5 10.5 L11 8.5 L15 10 L14.5 13 C14 14.5 12 15 10 14 C6 12 4 10 2 6 C1 4 1.5 2 3 1.5 Z" fill="var(--green)"/></svg>
    </p>
    <p class="contact-line">service@peltonridge.ca
      <svg viewBox="0 0 16 16" aria-hidden="true"><rect x="1" y="3" width="14" height="10" fill="none" stroke="var(--green)" stroke-width="1.5"/><path d="M1 3 L8 9 L15 3" fill="none" stroke="var(--green)" stroke-width="1.5"/></svg>
    </p>
    <p class="contact-line">www.peltonridge.ca
      <svg viewBox="0 0 16 16" aria-hidden="true"><circle cx="8" cy="8" r="6.5" fill="none" stroke="var(--green)" stroke-width="1.3"/><ellipse cx="8" cy="8" rx="3" ry="6.5" fill="none" stroke="var(--green)" stroke-width="1.1"/><path d="M1.5 8 H14.5" stroke="var(--green)" stroke-width="1.1"/></svg>
    </p>
    <div class="divider"></div>
    <ul class="services">
      <li>Furnace &amp; AC Repairs</li>
      <li>New Furnace &amp; AC Installation</li>
      <li>Ductwork</li>
      <li>Gas Lines</li>
      <li>Humidifiers</li>
      <li>Water Tanks</li>
      <li>Tankless Water Heaters</li>
    </ul>
  </div>
</section>

</body>
</html>
```